Business card design needed and matching letterhead

Internal medical specialist, specializing in allergy, respiratory and sleep medicine. Starting up practice, sending out business card to advertise to family doctors.
We are looking for a relatively simple business card design and letterhead, that will look elegant and professional. We would like the color scheme to be blue, and for it to involve circles/dots (abstract, but to look somewhat like an exploding pollen granule or mast cell).
The reverse side should just have a space for appointments, including date and time, and a line saying: if you are unable to attend your appointment, please contact us as soon as possible
Industry/Entity Type
Medical
Contact Information for Business Card
Dr Peter Hawksley MBBS FRACP
Airwell Clinic
482 Tallowood Rd
Wattledale 3281
Phone 6154 8291
Fax 5368 4175

```html
<!DOCTYPE html>
<html lang="en">
<head>
<meta charset="utf-8">
<title>Airwell Clinic – Business Card</title>
<link rel="stylesheet" href="https://fonts.googleapis.com/css2?family=Open+Sans:wght@400;600;700&display=swap">
<style>
  :root {
    --brand-blue: #1769ad;
    --card-grey: #ececec;
    --card-white: #f4f4f4;
    --ink: #3a3a3a;
    --rule: #8a8a8a;
    --backdrop: #e4e4e4;
  }
  * { box-sizing: border-box; margin: 0; padding: 0; }
  html, body {
    width: 1200px; height: 1000px; overflow: hidden;
    background: var(--backdrop);
    font-family: "Open Sans", Arial, sans-serif;
    color: var(--ink);
  }
  .sheet {
    width: 1200px; height: 1000px;
    display: flex; flex-direction: column; align-items: center; justify-content: center;
    gap: 44px;
  }
  .card {
    width: 760px; height: 436px;
    display: flex;
    box-shadow: 0 6px 18px rgba(0,0,0,0.12);
    overflow: hidden;
  }
  /* Front */
  .card-front__brand {
    width: 47%;
    background: var(--brand-blue);
    display: flex; align-items: center; justify-content: center;
  }
  .brand-lockup { display: flex; align-items: center; gap: 16px; }
  .brand-lockup__dot {
    width: 26px; height: 26px; border-radius: 50%;
    background: currentColor;
  }
  .brand-lockup__name {
    font-weight: 700; font-size: 40px; line-height: 1; letter-spacing: -0.5px;
  }
  .card-front__brand .brand-lockup { color: #ffffff; }
  .card-front__details {
    flex: 1;
    background: var(--card-grey);
    padding: 62px 0 0 0;
    position: relative;
  }
  .details-rule {
    position: absolute; left: 0; top: 70px;
    width: 30px; height: 1px; background: var(--rule);
  }
  .details { padding-left: 42px; font-size: 17px; line-height: 1.45; }
  .details__name { color: var(--brand-blue); font-weight: 600; font-size: 23px; line-height: 1.3; }
  .details__block { margin-bottom: 12px; }
  .details__label { color: var(--brand-blue); }

  /* Back */
  .card-back {
    background: var(--card-white);
    flex-direction: column;
    padding: 58px 70px 44px;
  }
  .card-back .brand-lockup { color: var(--brand-blue); margin-left: 60px; }
  .appointment { margin-top: 46px; flex: 1; }
  .appointment__row { display: flex; gap: 40px; margin-bottom: 36px; }
  .field { flex: 1; }
  .field__line { height: 1px; background: var(--rule); }
  .field__label { font-size: 13px; color: #666; margin-top: 4px; }
  .field--wide { flex: 2.4; }
  .field--time { flex: 1; }
  .field--day { flex: 1; }
  .field--date { flex: 1.3; }
  .card-back__notice {
    color: var(--brand-blue); font-weight: 600; font-size: 17px; text-align: center;
  }
</style>
</head>
<body>
<main class="sheet">
  <section class="card card-front" aria-label="Business card front">
    <div class="card-front__brand">
      <div class="brand-lockup">
        <span class="brand-lockup__dot"></span>
        <span class="brand-lockup__name">Airwell Clinic</span>
      </div>
    </div>
    <div class="card-front__details">
      <span class="details-rule"></span>
      <div class="details">
        <div class="details__block">
          <p class="details__name">Dr Peter Hawksley</p>
          <p>MBBS FRACP</p>
          <p>Consultant Physician</p>
        </div>
        <div class="details__block">
          <p>482 Tallowood Rd Wattledale 3281</p>
          <p><span class="details__label">Phone</span> 6154 8291</p>
          <p><span class="details__label">Fax</span> 5368 4175</p>
        </div>
      </div>
    </div>
  </section>

  <section class="card card-back" aria-label="Appointment card back">
    <div class="brand-lockup">
      <span class="brand-lockup__dot"></span>
      <span class="brand-lockup__name">Airwell Clinic</span>
    </div>
    <div class="appointment">
      <div class="appointment__row">
        <div class="field field--wide"><div class="field__line"></div><p class="field__label" style="text-align:center">your next appointment</p></div>
        <div class="field field--time"><div class="field__line"></div><p class="field__label" style="text-align:right">time</p></div>
      </div>
      <div class="appointment__row">
        <div class="field field--day"><div class="field__line"></div><p class="field__label">day</p></div>
        <div class="field field--date"><div class="field__line"></div><p class="field__label" style="text-align:center">date</p></div>
      </div>
    </div>
    <p class="card-back__notice">If you are unable to attend your appointment, please contact us as soon as possible</p>
  </section>
</main>
</body>
</html>
```